Coral Tidewave Stationary

Recently established Aquatics Club, with competitive swimming being a principal activity needs stationary, including business cards, letterhead and envelopes, application forms.
The designs shold incorporate the Club's logo. ( The colours are aqua and teal)
The statonary should be fun yet project a corporate image sufficient to attract potential sponsors.

Target Market(s)

Club members, sponsors, professional organisations.

Industry/Entity Type

Business

Requirements
Must have
• Club Logo
Address & Telephone number

The letterhead must contain the Club's Mission Statement.
It can be incorporated in the "footer" on the page.

To provide aquatics programmes, for persons of all ages, that encourage physical fitness and wellness, build character and self-discipline, inspire camaraderie and promote civic mindedness and excellence.

```html
<!DOCTYPE html>
<html lang="en">
<head>
<meta charset="utf-8">
<title>Coral Tidewave Business Card</title>
<link rel="stylesheet" href="https://fonts.googleapis.com/css2?family=Lato:wght@400;700&display=swap">
<style>
  :root {
    --teal: #22a9a3;
    --teal-deep: #178c87;
    --teal-light: #4cc3bc;
    --orange: #f08a24;
    --white: #ffffff;
    --backdrop: #e6eaeb;
    --shadow: rgba(20, 50, 55, 0.18);
  }
  * { box-sizing: border-box; margin: 0; padding: 0; }
  html, body { width: 1200px; height: 960px; overflow: hidden; }
  body {
    background: var(--backdrop);
    font-family: "Lato", sans-serif;
    position: relative;
  }
  .card {
    position: absolute;
    left: 250px;
    width: 700px;
    height: 400px;
    background: var(--white);
    box-shadow: 0 8px 24px var(--shadow);
    overflow: hidden;
  }
  .card--front { top: 50px; }
  .card--back { top: 500px; }
  .card__art { position: absolute; inset: 0; width: 100%; height: 100%; }

  .brand-name {
    position: absolute;
    color: var(--orange);
    font-weight: 400;
    white-space: nowrap;
  }
  .card--front .brand-name { left: 40px; top: 38px; font-size: 44px; }
  .card--back .brand-name {
    left: 0; right: 0; top: 168px;
    text-align: center; font-size: 62px;
  }

  .holder { position: absolute; left: 40px; top: 282px; color: var(--white); }
  .holder__name { font-size: 29px; font-weight: 400; }
  .holder__role { font-size: 20px; margin-top: 6px; }

  .contact {
    position: absolute; left: 418px; top: 240px;
    color: var(--white); font-size: 16px; line-height: 1.5;
  }
  .contact__row { display: flex; align-items: center; gap: 12px; }
  .contact__row svg { width: 13px; height: 13px; flex: none; }
  .contact__web { font-weight: 700; }
  .contact__address { margin-top: 18px; font-size: 16px; line-height: 1.45; }
</style>
</head>
<body>

<section class="card card--front" aria-label="Business card front">
  <svg class="card__art" viewBox="0 0 700 400" preserveAspectRatio="none" aria-hidden="true">
    <defs>
      <linearGradient id="bandFill" x1="0" y1="0" x2="0" y2="1">
        <stop offset="0" stop-color="#4cc3bc"/>
        <stop offset="1" stop-color="#178c87"/>
      </linearGradient>
    </defs>
    <path d="M0 232 C240 232 480 190 700 112 L700 400 L0 400 Z" fill="url(#bandFill)"/>
    <g fill="none" stroke="#22a9a3" stroke-width="3">
      <path d="M0 222 C240 222 480 180 700 102"/>
      <path d="M0 214 C240 214 480 172 700 94"/>
      <path d="M0 206 C240 206 480 164 700 86"/>
    </g>
  </svg>

  <div class="brand-name">Coral Tidewave</div>

  <div class="holder">
    <div class="holder__name">Marcus Ellery</div>
    <div class="holder__role">Manager</div>
  </div>

  <div class="contact">
    <div class="contact__row">
      <svg viewBox="0 0 16 16" aria-hidden="true"><path d="M3 1 L6 1 L7 5 L5 6.5 C6 9 7.5 10.5 9.5 11 L11 9 L15 10 L15 13 C15 14 14 15 13 15 C6.5 15 1 9.5 1 3 C1 2 2 1 3 1 Z" fill="#f08a24"/></svg>
      <span>555-014-2088</span>
    </div>
    <div class="contact__row">
      <svg viewBox="0 0 16 16" aria-hidden="true"><circle cx="8" cy="8" r="6.5" fill="none" stroke="#f08a24" stroke-width="2"/><path d="M1.5 8 H14.5 M8 1.5 C5 5 5 11 8 14.5 C11 11 11 5 8 1.5" fill="none" stroke="#f08a24" stroke-width="1.5"/></svg>
      <span class="contact__web">www.coraltidewave.com</span>
    </div>
    <div class="contact__address">48 Harbor Crest Road,<br>Lindale, PA 15999</div>
  </div>
</section>

<section class="card card--back" aria-label="Business card back">
  <svg class="card__art" viewBox="0 0 700 400" preserveAspectRatio="none" aria-hidden="true">
    <path d="M0 0 H700 V10 C480 22 240 30 0 32 Z" fill="#22a9a3"/>
    <g fill="none" stroke="#22a9a3" stroke-width="3">
      <path d="M0 40 C240 38 480 30 700 18"/>
      <path d="M0 48 C240 46 480 38 700 26"/>
      <path d="M0 56 C240 54 480 46 700 34"/>
    </g>
  </svg>
  <div class="brand-name">Coral Tidewave</div>
</section>

</body>
</html>
```